BBS Challenge Graphics for a Challenge

I want to create 9-10 social media graphics (new Instagram size 4:5 (1080 x 1350 pixels) focusing on our next 10-Day Berry Blend Sprint. Use any of the pics in the dropbox, NO RANDOM STOCK PHOTOGRAPHY. For the color scheme of the graphics, they should all be complementary to the green smoothie book attached.
You can add any of the photos as they are all posted here. You do NOT need to access Dropbox now. (all the details in the word document) NOTE: The date is Monday 12/8!
Updates

All of the images are now posted here. You do NOT need to access the Dropbox.

PLEASE NOTE THE DATE OF THIS CHALLENGE IS MONDAY, 12/8!

Target Market(s)

women and men

Requirements
Must have
• the text and pics in the Dropbox

```html
<!DOCTYPE html>
<html lang="en">
<head>
<meta charset="utf-8">
<title>10-Day Berry Blend Sprint – Social Set</title>
<link rel="stylesheet" href="https://fonts.googleapis.com/css2?family=Anton&family=Oswald:wght@500;700&family=Yellowtail&display=swap">
<style>
:root{
  --forest:#0d3f10;
  --deep:#16621b;
  --leaf:#2f9e3a;
  --grass:#4cbb3f;
  --lime:#8fd14f;
  --mint:#d3f0bf;
  --pale:#eef9e4;
  --sun:#f4e40c;
  --white:#ffffff;
  --skin:#6b4331;
  --pink:#e9b6c6;
  --wave-light:#5fc84a;
  --wave-dark:#1d7a24;
}
*{margin:0;padding:0;box-sizing:border-box}
html,body{width:1200px;height:3524px;overflow:hidden}
body{background:linear-gradient(180deg,#0a3a0c 0%,var(--forest) 50%,#0a3a0c 100%);font-family:'Anton',Impact,sans-serif;position:relative}

.set-title{position:absolute;top:18px;left:0;width:1200px;text-align:center;color:var(--white)}
.set-title__main{font-size:92px;line-height:1;letter-spacing:2px}
.set-title__script{font-family:'Yellowtail',cursive;color:var(--lime);font-size:64px;line-height:1;margin-top:-4px}

.grid{position:absolute;top:200px;left:56px;display:grid;grid-template-columns:524px 524px;column-gap:32px;row-gap:20px}
.post{position:relative;width:524px;height:640px;overflow:hidden;background:var(--leaf)}
.post svg.bg{position:absolute;inset:0;width:100%;height:100%}

.post--light{background:linear-gradient(160deg,var(--pale) 0%,var(--mint) 55%,var(--lime) 100%)}
.post--light::after{content:"";position:absolute;inset:14px;border:4px solid var(--white);pointer-events:none}
.post--green{background:linear-gradient(150deg,var(--grass) 0%,var(--leaf) 55%,var(--deep) 100%)}
.post--dark{background:linear-gradient(160deg,var(--deep) 0%,var(--forest) 100%)}

/* text blocks flow top-to-bottom so lines never collide */
.copy{position:absolute;display:flex;flex-direction:column;gap:12px;z-index:2}
.copy--center{align-items:center;text-align:center}
.copy--left{align-items:flex-start;text-align:left}
.head{text-transform:uppercase;line-height:.95}
.head--green{color:var(--deep)}
.head--white{color:var(--white)}
.sub{font-family:'Oswald',sans-serif;font-weight:700;text-transform:uppercase;line-height:1.15}
.sub--green{color:var(--deep)}
.sub--yellow{color:var(--sun)}
.sub--white{color:var(--white)}

.art{position:absolute}
.art--book{background:linear-gradient(160deg,#f5fbef 0%,#b7e08f 60%,#5fa63a 100%);border-radius:6px;box-shadow:6px 8px 14px rgba(0,0,0,.25)}
.art--bottle{background:linear-gradient(90deg,#d9dfd6 0%,#ffffff 45%,#c8d0c4 100%);border-radius:18px 18px 10px 10px;box-shadow:4px 8px 14px rgba(0,0,0,.25)}
.art--person{background:linear-gradient(180deg,#2a1a14 0%,var(--skin) 30%,var(--pink) 62%,#c97f97 100%);border-radius:48% 48% 0 0}
.art--person-dark{background:linear-gradient(180deg,#1e1411 0%,var(--skin) 30%,#222 60%,#111 100%);border-radius:48% 48% 0 0}
.sun{position:absolute;border-radius:50%;background:var(--sun)}
.banner{position:absolute;z-index:2;background:linear-gradient(90deg,var(--lime),var(--mint));color:var(--deep);text-align:center;text-transform:uppercase;display:flex;flex-direction:column;justify-content:center;gap:4px}
</style>
</head>
<body>

<header class="set-title">
  <div class="set-title__main">10-DAY BERRY</div>
  <div class="set-title__script">Blend Sprint</div>
</header>

<main class="grid">

  <!-- Row 1 -->
  <section class="post post--light">
    <div class="copy copy--center" style="top:44px;left:0;width:524px">
      <div class="head head--green" style="font-size:58px">10 - Day Berry<br>Blend Sprint</div>
      <div class="sub sub--green" style="font-size:26px">Begins Monday 12/8!<br>Lose up to 15lbs in 10 days!</div>
    </div>
    <div class="art art--book" style="left:140px;top:330px;width:190px;height:250px;transform:rotate(-8deg)" role="img" aria-label="Berry Blend Reset book cover"></div>
    <div class="art art--book" style="left:250px;top:345px;width:170px;height:230px;transform:rotate(6deg)" role="img" aria-label="Berry Blend Reset book cover, second copy"></div>
  </section>

  <section class="post post--green">
    <svg class="bg" viewBox="0 0 524 640" aria-hidden="true"><path d="M0 0H524V180C420 230 380 120 280 170S120 260 0 210Z" fill="var(--wave-light)"/><path d="M0 470C120 420 200 520 320 480S460 420 524 450V640H0Z" fill="var(--wave-dark)"/></svg>
    <div class="copy copy--left" style="top:40px;left:34px;width:260px">
      <div class="head head--white" style="font-size:84px">10-Day<br>Berry<br>Blend</div>
      <div class="sub sub--white" style="font-size:17px">Sprint + Berry Blend Bites™</div>
    </div>
    <div class="art art--bottle" style="left:300px;top:300px;width:110px;height:190px" role="img" aria-label="Berry Blend Bites bottle"></div>
    <div class="art art--bottle" style="left:380px;top:280px;width:110px;height:210px" role="img" aria-label="Berry Blend Bites bottle, second"></div>
    <div class="copy copy--left" style="top:520px;left:36px;width:240px">
      <div class="sub sub--white" style="font-size:22px">Begins Monday 12/8<br>Join us</div>
    </div>
  </section>

  <!-- Row 2 -->
  <section class="post post--light">
    <div class="copy copy--center" style="top:40px;left:0;width:524px;gap:6px">
      <div class="head head--green" style="font-size:82px">10-Day</div>
      <div class="head head--green" style="font-size:50px">Berry Blend Sprint</div>
    </div>
    <div class="copy copy--left" style="top:256px;left:40px;width:200px">
      <div class="sub sub--green" style="font-size:22px">Begins Monday 12/8!<br>Lose up to<br>15lbs in 10 days!</div>
    </div>
    <div class="art art--person" style="left:250px;top:240px;width:250px;height:400px" role="img" aria-label="Smiling woman holding the Berry Blend Reset book"></div>
  </section>

  <section class="post post--green">
    <svg class="bg" viewBox="0 0 524 640" aria-hidden="true"><path d="M0 120C140 60 240 200 380 140S500 60 524 90V0H0Z" fill="var(--wave-light)"/><path d="M0 520C160 480 260 600 524 540V640H0Z" fill="var(--wave-dark)"/></svg>
    <div class="copy copy--left" style="top:150px;left:34px;width:280px">
      <div class="head head--white" style="font-size:76px">10-Day<br>Berry<br>Blend</div>
      <div class="sub sub--white" style="font-size:16px">Sprint + Berry Blend Bites™</div>
      <div class="sub sub--yellow" style="font-size:22px">Begins Monday 12/8<br>Join us</div>
    </div>
    <div class="art art--bottle" style="left:330px;top:220px;width:150px;height:270px" role="img" aria-label="Berry Blend Bites bottle"></div>
  </section>

  <!-- Row 3 -->
  <section class="post post--light">
    <div class="sun" style="left:36px;top:36px;width:110px;height:110px"></div>
    <div class="art art--bottle" style="left:300px;top:170px;width:180px;height:270px" role="img" aria-label="Berry Blend Bites bottle"></div>
    <div class="copy copy--left" style="top:190px;left:40px;width:250px">
      <div class="head head--green" style="font-size:62px">10-Day<br>Berry<br>Blend<br>Sprint</div>
    </div>
    <div class="copy copy--center" style="top:520px;left:0;width:524px">
      <div class="sub sub--green" style="font-size:22px">Begins Monday 12/8!<br>Lose up to 15lbs in 10 days!</div>
    </div>
  </section>

  <section class="post post--green">
    <svg class="bg" viewBox="0 0 524 640" aria-hidden="true"><path d="M0 330C120 290 220 390 360 350S480 290 524 310V640H0Z" fill="var(--wave-dark)"/></svg>
    <div class="copy copy--center" style="top:36px;left:0;width:524px;gap:10px">
      <div class="head head--white" style="font-size:80px">10-Day<br>Berry Blend</div>
      <div class="sub sub--white" style="font-size:18px">Sprint + Berry Blend Bites™</div>
      <div class="sub sub--yellow" style="font-size:22px">Begins Monday 12/8<br>Join us</div>
    </div>
    <div class="art art--book" style="left:110px;top:380px;width:160px;height:220px;transform:rotate(-6deg)" role="img" aria-label="Berry Blend Reset book cover"></div>
    <div class="art art--book" style="left:240px;top:390px;width:160px;height:220px;transform:rotate(6deg)" role="img" aria-label="Berry Blend Reset book cover, second copy"></div>
  </section>

  <!-- Row 4 -->
  <section class="post post--dark">
    <svg class="bg" viewBox="0 0 524 640" aria-hidden="true"><path d="M300 0H524V640H360C300 500 420 360 320 220S280 60 300 0Z" fill="var(--leaf)"/></svg>
    <div class="copy copy--left" style="top:44px;left:30px;width:220px">
      <div class="head head--white" style="font-size:64px">10-Day<br>Berry<br>Blend<br>Sprint</div>
      <div class="sub sub--yellow" style="font-size:20px">Begins Monday 12/8!<br>Lose up to<br>15lbs in 10 days!</div>
    </div>
    <div class="art art--person" style="left:260px;top:70px;width:250px;height:570px" role="img" aria-label="Smiling woman holding the Berry Blend Reset book"></div>
    <div class="art art--bottle" style="left:60px;top:460px;width:110px;height:150px" role="img" aria-label="Berry Blend Bites bottle"></div>
  </section>

  <section class="post post--green">
    <svg class="bg" viewBox="0 0 524 640" aria-hidden="true"><path d="M0 0H524V120C400 180 300 60 200 110S60 180 0 140Z" fill="var(--wave-light)"/></svg>
    <div class="art art--person" style="left:20px;top:80px;width:230px;height:560px" role="img" aria-label="Smiling woman holding a Berry Blend Bites bottle"></div>
    <div class="copy copy--center" style="top:290px;left:262px;width:250px;gap:10px">
      <div class="head head--white" style="font-size:58px">10-Day<br>Berry<br>Blend</div>
      <div class="sub sub--white" style="font-size:14px">Sprint + Berry Blend Bites™</div>
      <div class="sub sub--yellow" style="font-size:19px">Begins Monday 12/8<br>Join us</div>
    </div>
  </section>

  <!-- Row 5 -->
  <section class="post post--green">
    <svg class="bg" viewBox="0 0 524 640" aria-hidden="true"><path d="M524 0V200C420 240 360 140 260 160S120 120 80 0Z" fill="var(--wave-light)"/><path d="M0 560C180 520 320 600 524 560V640H0Z" fill="var(--wave-dark)"/></svg>
    <div class="art art--person" style="left:10px;top:60px;width:240px;height:580px" role="img" aria-label="Smiling woman in pink holding a Berry Blend Bites bottle"></div>
    <div class="copy copy--center" style="top:300px;left:256px;width:258px;gap:8px">
      <div class="head head--white" style="font-size:68px">10-Day<br>Berry</div>
      <div class="head head--white" style="font-size:30px">Blend Sprint</div>
      <div class="sub sub--yellow" style="font-size:16px">Begins Monday 12/8!<br>Lose up to 15lbs in 10 days!</div>
    </div>
  </section>

  <section class="post post--green">
    <svg class="bg" viewBox="0 0 524 640" aria-hidden="true"><path d="M0 0H524V160C420 120 360 220 260 180S100 80 0 130Z" fill="var(--wave-light)"/></svg>
    <div class="art art--person-dark" style="left:132px;top:70px;width:260px;height:400px" role="img" aria-label="Woman in a black top holding a Berry Blend Bites bottle"></div>
    <div class="banner" style="left:52px;top:460px;width:420px;height:100px">
      <div style="font-size:44px;line-height:1">10-Day Berry Blend</div>
      <div style="font-family:'Oswald',sans-serif;font-weight:700;font-size:15px">Sprint + Berry Blend Bites™</div>
    </div>
    <div class="copy copy--center" style="top:584px;left:0;width:524px">
      <div class="sub sub--white" style="font-size:22px">Begins Monday 12/8 Join us</div>
    </div>
  </section>

</main>
</body>
</html>
```